Business Card *

A business card design
Use the logo uploaded in the brief page.
You may use placeholders in your design layouts.
I will provide the actual business card details to the winning designer.

Logo
Place for contact info (name, title, phone, email, etc)

Requirements
Must have
• Logo

```html
<!DOCTYPE html>
<html lang="en">
<head>
<meta charset="utf-8">
<title>Harrowfield Business Card</title>
<link rel="stylesheet" href="https://fonts.googleapis.com/css2?family=Raleway:wght@600;700;800&family=Open+Sans:wght@400&display=swap">
<style>
  :root {
    --stage: #9bfb94;
    --leaf: #88c540;
    --leaf-pale: #cde4ad;
    --paper: #ffffff;
    --ink-grey: #8c8c8c;
    --ghost: #e2e2e2;
    --white: #ffffff;
  }
  * { box-sizing: border-box; margin: 0; padding: 0; }
  html, body { width: 1200px; height: 507px; overflow: hidden; }
  body { background: var(--stage); position: relative; }

  .card {
    position: absolute;
    top: 79px;
    width: 536px;
    height: 346px;
    background: var(--paper);
    overflow: hidden;
    box-shadow: 0 4px 14px rgba(40, 110, 40, 0.25);
  }
  .card--front { left: 48px; }
  .card--back { left: 617px; }

  .card__arc { position: absolute; inset: 0; }

  .ghost-ring {
    position: absolute;
    top: 25px;
    width: 280px;
    height: 280px;
    border-radius: 50%;
    border: 14px solid var(--ghost);
  }
  .card--front .ghost-ring { left: 396px; }
  .card--back .ghost-ring { left: -140px; }

  .brand {
    position: absolute;
    display: flex;
    align-items: center;
    gap: 8px;
    font-family: "Raleway", sans-serif;
    font-weight: 800;
    letter-spacing: 0.5px;
    white-space: nowrap;
  }
  .brand__dot {
    width: 20px;
    height: 20px;
    border-radius: 50%;
    background: var(--leaf);
  }
  .card--front .brand {
    left: 150px;
    top: 158px;
    font-size: 23px;
    color: var(--ink-grey);
  }

  .back__stripe {
    position: absolute;
    left: 247px;
    top: 0;
    width: 22px;
    height: 100%;
    background: var(--leaf-pale);
  }
  .back__panel {
    position: absolute;
    left: 269px;
    top: 0;
    right: 0;
    height: 100%;
    background: var(--leaf);
    color: var(--white);
  }
  .back__panel .brand {
    left: 37px;
    top: 104px;
    font-size: 20px;
    color: var(--white);
  }
  .person { position: absolute; left: 37px; top: 196px; font-family: "Raleway", sans-serif; }
  .person__name { font-weight: 700; font-size: 21px; letter-spacing: 0.3px; }
  .person__title { font-weight: 600; font-size: 16px; margin-top: 2px; letter-spacing: 0.5px; }

  .contacts {
    position: absolute;
    left: 37px;
    top: 263px;
    list-style: none;
    font-family: "Open Sans", sans-serif;
    font-size: 13px;
    line-height: 19px;
  }
  .contacts li { display: flex; align-items: center; gap: 6px; }
  .contacts svg { width: 11px; height: 11px; fill: var(--white); }
</style>
</head>
<body>
  <section class="card card--front">
    <svg class="card__arc" viewBox="0 0 536 346" width="536" height="346" aria-hidden="true">
      <path d="M0 0 H112 Q-4 173 112 346 H0 Z" fill="var(--leaf-pale)"/>
      <path d="M0 0 H92 Q-22 173 92 346 H0 Z" fill="var(--leaf)"/>
    </svg>
    <div class="ghost-ring" aria-hidden="true"></div>
    <div class="brand"><span class="brand__dot"></span>HARROWFIELD</div>
  </section>

  <section class="card card--back">
    <div class="ghost-ring" aria-hidden="true"></div>
    <div class="back__stripe"></div>
    <div class="back__panel">
      <div class="brand">HARROWFIELD</div>
      <div class="person">
        <p class="person__name">NAME SURNAME</p>
        <p class="person__title">TITLE</p>
      </div>
      <ul class="contacts">
        <li>
          <svg viewBox="0 0 24 24" aria-hidden="true"><path d="M6.6 10.8a15.1 15.1 0 0 0 6.6 6.6l2.2-2.2a1 1 0 0 1 1-.25 11.4 11.4 0 0 0 3.6.57 1 1 0 0 1 1 1V20a1 1 0 0 1-1 1A17 17 0 0 1 3 4a1 1 0 0 1 1-1h3.5a1 1 0 0 1 1 1c0 1.25.2 2.45.57 3.570a1 1 0 0 1-.25 1z"/></svg>
          09876543210
        </li>
        <li>
          <svg viewBox="0 0 24 24" aria-hidden="true"><path d="M2 5h20v14H2z" fill="var(--white)"/><path d="M3 6l9 7 9-7" fill="none" stroke="var(--leaf)" stroke-width="2"/></svg>
          name@harrowfield.example
        </li>
      </ul>
    </div>
  </section>
</body>
</html>
```